Bramblewick Affairs Web Design Project

This is a bit of a challenging request. Bramblewick Affairs (event planning) and ORB Gala Hireworks (event equipment rental), operate in the Northern Virginia area and we are in the process of marketing ourselves heavily as a "on stop celebration shop". Our customers range from large music festivals to smaller corporate functions. We are seeking to integrate two companies under one umbrella, our event planning company which also offers catering services " Bramblewick Affair, LLC" with our event rental equipment company "ORB Gala Hireworks." Both have new logos created through Pixel Harbor. I would like to have one portal that provides access to both companies and maintain the party rental URL as a stand alone to remain accessible to our loyal customers if possible. The only website that exist today is ORB Gala Hireworks with the URL (www.orbgalahub.example), which needs a complete redesign, as it is very antiquated. This URL should still be able to stand on its own as well as integrated/accessible into the new overall parent company BRamblewick Affairs/ Our goal is to is to communicate to our customers that we are energetic, modern company with fresh celebration ideas and the hardware to go with it. There are numerous photos that need to be uploaded to the rental part of site. We will need to be able to update and make changes to photos without outside support.

Reason: I am changing the project to being a non-refundable and hope to get more submissions.

Target Market(s)

A very broad range of customers, from large rock festivals, to small country weddings and corporate functions

Industry/Entity Type

Event Planning

Requirements
Must have
• Must Have:
- - Ability to add and update photos without external support
-Modern interface ( look and feel)
-Easy user centered design
- multiple sections ( tabs) such as , Home, Event Planning, Catering, Galleries, Venues, Contact Us
Nice to have
• - ability to place event rental orders online

```html
<!DOCTYPE html>
<html lang="en">
<head>
<meta charset="utf-8">
<title>ORB Gala Hireworks</title>
<link href="https://fonts.googleapis.com/css2?family=Source+Sans+3:wght@400;600;700&display=swap" rel="stylesheet">
<style>
  :root{
    --orange:#f47835;
    --orange-dark:#e85f22;
    --purple:#5b3fa0;
    --purple-dark:#4a3189;
    --text:#555;
    --rule:#e2e2e2;
    --white:#fff;
    --field-text:#666;
    --btn:#3f3f3f;
  }
  *{box-sizing:border-box;margin:0;padding:0}
  html,body{width:1200px;height:1020px;overflow:hidden;background:var(--white);font-family:"Source Sans 3",sans-serif;color:var(--text)}
  .page{position:relative;width:1200px;height:1020px}
  .topbar{position:absolute;left:0;top:0;width:1200px;height:25px;background:var(--orange);color:var(--white);font-size:13px;font-weight:700}
  .topbar .phone{position:absolute;left:120px;top:4px}
  .topbar .email{position:absolute;right:121px;top:4px}
  .brand{position:absolute;display:flex;align-items:center;gap:12px}
  .brand-rentals{left:120px;top:31px}
  .brand-rentals .mark{width:75px;height:75px;border-radius:50%;background:var(--purple)}
  .brand-rentals .name{font-size:34px;font-weight:700;color:var(--orange);letter-spacing:.5px}
  .brand-events{right:120px;top:46px}
  .brand-events .name{font-size:34px;font-weight:600;color:var(--purple)}
  .nav{position:absolute;left:120px;top:119px;width:960px;height:40px;background:var(--purple);display:flex;list-style:none;border:1px solid var(--purple-dark)}
  .nav li{color:var(--white);font-size:16px;font-weight:600;line-height:38px;text-align:center}
  .nav li.active{background:var(--orange)}
  .hero{position:absolute;left:120px;top:159px;width:960px;height:330px;background:radial-gradient(ellipse at 50% 75%,#b8864a 0%,#6a2d14 40%,#2a0c06 80%,#140504 100%)}
  .dots{position:absolute;left:572px;top:464px;display:flex;gap:6px}
  .dots span{width:9px;height:9px;border-radius:50%;background:#8a8a8a;border:1px solid #bbb}
  .welcome{position:absolute;left:120px;top:505px;width:960px;text-align:center}
  .welcome h1{font-size:22px;font-weight:600;color:var(--purple);margin-bottom:13px}
  .welcome p{font-size:13px;line-height:17px}
  .welcome .tag{margin-top:17px}
  .rule{position:absolute;left:120px;width:960px;height:3px;border-top:1px solid var(--rule);border-bottom:1px solid var(--rule)}
  .section-title{position:absolute;font-size:22px;font-weight:600;color:var(--purple)}
  .photo{position:absolute}
  .video{left:120px;top:733px;width:330px;height:220px;background:radial-gradient(ellipse at 60% 50%,#e8c878 0%,#a06a28 45%,#4a200c 100%)}
  .play{position:absolute;left:122px;top:83px;width:82px;height:56px;border-radius:10px;background:#222;border:2px solid #555}
  .play::after{content:"";position:absolute;left:30px;top:13px;border-left:24px solid #ddd;border-top:14px solid transparent;border-bottom:14px solid transparent}
  .gallery-main{left:470px;top:733px;width:330px;height:130px;background:linear-gradient(180deg,#3a3a3a 0%,#9a9a9a 55%,#e8e8e8 100%)}
  .thumb{top:872px;width:100px;height:80px}
  .t1{left:470px;background:linear-gradient(180deg,#555 0%,#cfcfcf 100%)}
  .t2{left:585px;background:linear-gradient(180deg,#6a2a1a 0%,#c86a3a 60%,#e6c6a0 100%)}
  .t3{left:700px;background:linear-gradient(180deg,#7a3a20 0%,#b0603a 50%,#e0c0a8 100%)}
  .order{position:absolute;left:820px;top:686px;width:260px;height:267px;background:linear-gradient(180deg,var(--orange) 0%,var(--orange-dark) 100%);border:1px solid #e0642a}
  .order h2{position:absolute;left:9px;top:8px;font-size:21px;font-weight:400;color:var(--white)}
  .field{position:absolute;background:var(--white);height:37px;font-size:13px;font-weight:600;color:var(--field-text);padding:12px 5px 0}
  .f-name{left:9px;top:42px;width:240px}
  .f-date{left:9px;top:87px;width:240px}
  .f-date svg{position:absolute;right:10px;top:8px}
  .f-t1{left:9px;top:132px;width:100px}
  .f-t2{left:149px;top:132px;width:100px}
  .to{position:absolute;left:122px;top:148px;color:var(--white);font-size:13px;font-weight:600}
  .f-sel{left:9px;top:177px;width:240px}
  .f-sel::after{content:"";position:absolute;right:12px;top:15px;border-top:7px solid #aaa;border-left:4px solid transparent;border-right:4px solid transparent}
  .submit{position:absolute;left:149px;top:222px;width:100px;height:37px;background:var(--btn);color:var(--white);font-size:17px;font-weight:600;text-align:center;line-height:37px;border:1px solid #2a2a2a}
  .copy{position:absolute;left:120px;top:989px;font-size:11px}
  .social{position:absolute;top:989px;display:flex;gap:6px;left:967px}
  .social span{width:24px;height:24px}
  .s1{background:#3b5998}.s2{background:#29a9e1}.s3{background:#d22a1e}.s4{background:#333}
</style>
</head>
<body>
<div class="page">
  <header class="topbar">
    <span class="phone">Phone: (703) 555-0148</span>
    <span class="email">Email :info@orbgalahub.example</span>
  </header>

  <div class="brand brand-rentals"><span class="mark"></span><span class="name">ORB Gala Hireworks</span></div>
  <div class="brand brand-events"><span class="name">Bramblewick Affairs</span></div>

  <ul class="nav">
    <li class="active" style="width:120px">HOME</li>
    <li style="width:215px">EVENT PLANNING</li>
    <li style="width:147px">CATERING</li>
    <li style="width:165px">GALLERIES</li>
    <li style="width:135px">VENUES</li>
    <li style="width:178px">CONTACT US</li>
  </ul>

  <div class="hero" role="img" aria-label="Banquet hall with round tables set for an event, warm lighting"></div>
  <div class="dots"><span></span><span></span><span></span><span></span></div>

  <section class="welcome">
    <h1>Welcome to Orchard Ridge Banquets (ORB) Gala Hireworks</h1>
    <p>Serving Northern Virginia Party Needs Since 1999!<br>
    Let Orchard Ridge Banquets (ORB) Gala Hireworks make your next wedding, private party, corporate event, or special occasion a memorable one.<br>
    Please browse our products and services here or contact one of our knowledgeable staff members for ideas and/or assistance.<br>
    In any season, indoor or outdoor,</p>
    <p class="tag">"We've Got You Covered!"</p>
  </section>

  <div class="rule" style="top:662px"></div>

  <h2 class="section-title" style="left:120px;top:690px">How it works</h2>
  <div class="photo video" role="img" aria-label="Glasses of champagne on a table with candles, video preview">
    <span class="play"></span>
  </div>

  <h2 class="section-title" style="left:470px;top:690px">Photo Gallery</h2>
  <div class="photo gallery-main" role="img" aria-label="Table setting with glassware and plates"></div>
  <div class="photo thumb t1" role="img" aria-label="Round table set for a reception"></div>
  <div class="photo thumb t2" role="img" aria-label="Long table with flowers and candles"></div>
  <div class="photo thumb t3" role="img" aria-label="Banquet room filled with dining tables"></div>

  <form class="order">
    <h2>Rental orders online</h2>
    <div class="field f-name">Enter your Name</div>
    <div class="field f-date">Select Date
      <svg width="17" height="20" viewBox="0 0 17 20"><rect x="0" y="2" width="17" height="18" fill="#555"/><rect x="3" y="0" width="2" height="4" fill="#555"/><rect x="12" y="0" width="2" height="4" fill="#555"/><g fill="#fff"><rect x="2" y="7" width="3" height="3"/><rect x="7" y="7" width="3" height="3"/><rect x="12" y="7" width="3" height="3"/><rect x="2" y="12" width="3" height="3"/><rect x="7" y="12" width="3" height="3"/><rect x="12" y="12" width="3" height="3"/></g></svg>
    </div>
    <div class="field f-t1">Time</div>
    <span class="to">to</span>
    <div class="field f-t2">Time</div>
    <div class="field f-sel">Select any</div>
    <div class="submit">SUBMIT</div>
  </form>

  <div class="rule" style="top:974px"></div>
  <footer>
    <p class="copy">© 2013 Orchard Ridge Banquets (ORB) Gala Hireworks</p>
    <div class="social"><span class="s1"></span><span class="s2"></span><span class="s3"></span><span class="s4"></span></div>
  </footer>
</div>
</body>
</html>
```